Keys to business success

I love the principles of a book called "Where the quiet rivers bend toward home". I use the principles all the time at work. I'd like a poster made (map or web style design) to capture the books reminders. You can see a very basic verison of the design i'm looking for attached below "project summary".I've attached a word document of the text to include. Ive also attached two examples of the types of designs i'm looking for. The design will have to look modern and clear when printed on an 45.7 x 61 cm canvas.

Target Market(s)

Buisness people
Motivation

Industry/Entity Type

Business

Font styles to use
Serif

Requirements
Must have
• Web or map-like designs
• All 30 of the principles: 3 fonts (Title, sub-title and principles). The choice of fonts is up to the designer. No numbers for the principles.
• Professional feel
Nice to have
• Halos around phrases
Should not have
• No straight lines or ridgid concepts

```html
<!DOCTYPE html>
<html lang="en">
<head>
<meta charset="utf-8">
<title>Principles Web Poster</title>
<link href="https://fonts.googleapis.com/css2?family=Cormorant+Garamond:wght@600;700&family=Playfair+Display:wght@700;800&family=Roboto+Serif:opsz,wdth,wght@8..144,50..150,100..900&display=swap" rel="stylesheet">
<style>
  :root {
    --bg-dark: #121212;
    --bg-mid: #242424;
    --line-blue: #9ad8f2;
    --ring-blue: #7fc4e4;
    --ring-deep: #3d6f86;
    --disc-top: #5a5a5a;
    --disc-bottom: #262626;
    --text-light: #f2f2f2;
    --subtitle-fill: #1a1a1a;
    --subtitle-edge: #d6d6d6;
    --panel-black: #050505;
  }
  html, body {
    margin: 0;
    padding: 0;
    width: 1200px;
    height: 899px;
    overflow: hidden;
  }
  body {
    background: radial-gradient(ellipse at 45% 45%, var(--bg-mid) 0%, var(--bg-dark) 80%);
  }
  .poster {
    display: block;
    width: 1200px;
    height: 899px;
  }
  .branch { fill: none; stroke: var(--line-blue); stroke-width: 3; stroke-linecap: round; }
  .frame-outer { fill: none; stroke: var(--line-blue); stroke-width: 4; }
  .frame-inner { fill: none; stroke: var(--ring-blue); stroke-width: 2; }
  .frame-panel { fill: var(--panel-black); }
  .principle {
    fill: var(--text-light);
    font-family: "Roboto Serif", Georgia, serif;
    font-stretch: 50%;
    font-variation-settings: "wdth" 50, "opsz" 14;
    font-weight: 500;
    font-size: 15px;
  }
  .hub-ring-outer { fill: none; stroke: var(--ring-blue); stroke-width: 2; opacity: .8; }
  .hub-ring-mid { fill: none; stroke: var(--line-blue); stroke-width: 3; }
  .hub-ring-band { fill: none; stroke: var(--ring-deep); stroke-width: 7; }
  .hub-ring-inner { fill: none; stroke: #cfd8dc; stroke-width: 1.5; }
  .hub-disc { fill: url(#disc-shade); }
  .hub-title {
    fill: var(--text-light);
    text-anchor: middle;
    font-family: "Roboto Serif", Georgia, serif;
    font-stretch: 50%;
    font-variation-settings: "wdth" 50, "opsz" 36;
    font-weight: 700;
  }
  .count {
    font-family: "Playfair Display", Georgia, serif;
    font-weight: 800;
    font-variant-numeric: lining-nums;
    font-size: 190px;
    text-anchor: middle;
    fill: url(#count-shade);
    stroke: #8a8a8a;
    stroke-width: 1.5;
  }
  .subtitle {
    font-family: "Cormorant Garamond", Georgia, serif;
    font-weight: 700;
    font-size: 22px;
    text-anchor: middle;
    fill: var(--subtitle-fill);
    stroke: var(--subtitle-edge);
    stroke-width: .8;
    letter-spacing: 2px;
  }
</style>
</head>
<body>
<svg class="poster" viewBox="0 0 1200 899" xmlns="http://www.w3.org/2000/svg" role="img" aria-label="Web of thirty principles grouped around four hubs">
  <defs>
    <radialGradient id="disc-shade" cx="45%" cy="30%" r="75%">
      <stop offset="0%" stop-color="#5a5a5a"/>
      <stop offset="100%" stop-color="#262626"/>
    </radialGradient>
    <linearGradient id="count-shade" x1="0" y1="0" x2="0" y2="1">
      <stop offset="0%" stop-color="#ffffff"/>
      <stop offset="55%" stop-color="#e4e4e4"/>
      <stop offset="100%" stop-color="#9a9a9a"/>
    </linearGradient>
    <filter id="glow" x="-20%" y="-20%" width="140%" height="140%">
      <feGaussianBlur stdDeviation="2.5" result="b"/>
      <feMerge><feMergeNode in="b"/><feMergeNode in="SourceGraphic"/></feMerge>
    </filter>
  </defs>

  <g class="centre-panel">
    <rect class="frame-outer" x="138" y="320" width="486" height="281" rx="26" filter="url(#glow)"/>
    <rect class="frame-inner" x="147" y="329" width="468" height="263" rx="20"/>
    <rect class="frame-panel" x="155" y="337" width="452" height="247" rx="14"/>
    <text class="count" x="381" y="508" textLength="170" lengthAdjust="spacingAndGlyphs">30</text>
    <text class="subtitle" x="381" y="568" textLength="440" lengthAdjust="spacingAndGlyphs">PRINCIPLES · WHERE THE QUIET RIVERS BEND TOWARD HOME</text>
  </g>

  <g class="branches" filter="url(#glow)">
    <path class="branch" d="M190 22 C182 90 198 160 188 220 C184 250 192 275 190 290"/>
    <path class="branch" d="M190 22 Q201 16 214 22 M191 56 Q202 50 214 56 M191 89 Q202 83 214 89 M192 123 Q203 117 214 123 M192 156 Q203 150 214 156 M191 189 Q202 183 214 189 M189 222 Q201 216 214 222 M188 256 Q201 250 214 256 M190 290 Q202 284 214 290"/>
    <path class="branch" d="M652 355 C660 385 644 420 652 460"/>
    <path class="branch" d="M653 393 Q662 387 670 393 M651 426 Q661 420 670 426 M652 460 Q661 454 670 460"/>
    <path class="branch" d="M190 650 Q200 642 210 648 Q218 652 226 650"/>
    <path class="branch" d="M210 650 C202 700 218 760 210 817"/>
    <path class="branch" d="M211 683 Q218 677 226 683 M212 717 Q219 711 226 717 M211 750 Q218 744 226 750 M210 783 Q218 777 226 783 M210 817 Q218 811 226 817"/>
    <path class="branch" d="M760 505 C768 600 752 700 762 790 C766 830 758 850 760 870"/>
    <path class="branch" d="M760 505 Q768 499 776 505 M761 538 Q769 532 776 538 M762 571 Q769 565 776 571 M763 604 Q770 598 776 604 M763 637 Q770 631 776 637 M762 671 Q769 665 776 671 M761 704 Q769 698 776 704 M760 737 Q768 731 776 737 M760 770 Q768 764 776 770 M762 803 Q769 797 776 803 M762 837 Q769 831 776 837 M760 870 Q768 864 776 870"/>
  </g>

  <g class="principle-list leader">
    <text class="principle" x="228" y="28" textLength="228" lengthAdjust="spacingAndGlyphs">BEGIN WITH PRAISE AND HONEST APPRECIATION</text>
    <text class="principle" x="228" y="62" textLength="249" lengthAdjust="spacingAndGlyphs">CALL ATTENTION TO PEOPLE'S MISTAKES INDIRECTLY</text>
    <text class="principle" x="228" y="95" textLength="357" lengthAdjust="spacingAndGlyphs">TALK ABOUT YOUR OWN MISTAKES BEFORE CRITICIZING THE OTHER PERSON</text>
    <text class="principle" x="228" y="129" textLength="246" lengthAdjust="spacingAndGlyphs">ASK QUESTIONS INSTEAD OF GIVING DIRECT ORDERS</text>
    <text class="principle" x="228" y="162" textLength="161" lengthAdjust="spacingAndGlyphs">LET THE OTHER PERSON SAVE FACE</text>
    <text class="principle" x="228" y="195" textLength="357" lengthAdjust="spacingAndGlyphs">PRAISE THE SLIGHTEST IMPROVEMENT AND PRAISE EVERY IMPROVEMENT.</text>
    <text class="principle" x="228" y="228" textLength="273" lengthAdjust="spacingAndGlyphs">GIVE THE OTHER PERSON A FINE REPUTATION TO LIVE UP TO</text>
    <text class="principle" x="228" y="262" textLength="307" lengthAdjust="spacingAndGlyphs">USE ENCOURAGEMENT. MAKE THE FAULT SEEM EASY TO CORRECT</text>
    <text class="principle" x="228" y="296" textLength="342" lengthAdjust="spacingAndGlyphs">MAKE THE OTHER PERSON HAPPY ABOUT DOING THE THING YOU SUGGEST</text>
  </g>

  <g class="principle-list fundamentals">
    <text class="principle" x="678" y="399" textLength="230" lengthAdjust="spacingAndGlyphs">DON'T CRITICIZE, CONDEMN OR COMPLAIN</text>
    <text class="principle" x="678" y="432" textLength="216" lengthAdjust="spacingAndGlyphs">GIVE HONEST, SINCERE, APPRECIATION</text>
    <text class="principle" x="678" y="466" textLength="259" lengthAdjust="spacingAndGlyphs">AROUSE IN THE OTHER PERSON AN EAGER WANT</text>
  </g>

  <g class="principle-list liking">
    <text class="principle" x="243" y="656" textLength="289" lengthAdjust="spacingAndGlyphs">BECOME GENUINELY INTERESTED IN OTHER PEOPLE SMILE</text>
    <text class="principle" x="243" y="689" textLength="254" lengthAdjust="spacingAndGlyphs">A PERSON'S NAME IS TO THAT PERSON THE SWEETEST</text>
    <text class="principle" x="243" y="723" textLength="154" lengthAdjust="spacingAndGlyphs">AND MOST IMPORTANT SOUND</text>
    <text class="principle" x="243" y="756" textLength="365" lengthAdjust="spacingAndGlyphs">BE A GOOD LISTENER. ENCOURAGE OTHERS TO TALK ABOUT THEMSELVES</text>
    <text class="principle" x="243" y="789" textLength="262" lengthAdjust="spacingAndGlyphs">TALK IN TERMS OF THE OTHER PERSON'S INTERESTS</text>
    <text class="principle" x="243" y="823" textLength="335" lengthAdjust="spacingAndGlyphs">MAKE THE OTHER PERSON FEEL IMPORTANT – AND DO IT SINCERELY</text>
  </g>

  <g class="principle-list persuasion">
    <text class="principle" x="785" y="511" textLength="323" lengthAdjust="spacingAndGlyphs">THE ONLY WAY TO GET THE BEST OF AN ARGUMENT IS TO AVOID IT</text>
    <text class="principle" x="785" y="544" textLength="402" lengthAdjust="spacingAndGlyphs">SHOW RESPECT FOR THE OTHER PERSON'S OPINION. NEVER SAY, "YOU'RE WRONG."</text>
    <text class="principle" x="785" y="577" textLength="281" lengthAdjust="spacingAndGlyphs">IF YOU ARE WRONG ADMIT IT QUICKLY AND EMPHATICALLY</text>
    <text class="principle" x="785" y="610" textLength="145" lengthAdjust="spacingAndGlyphs">BEGIN IN A FRIENDLY MANNER</text>
    <text class="principle" x="785" y="643" textLength="211" lengthAdjust="spacingAndGlyphs">GET THE OTHER PERSON SAYING "YES, YES"</text>
    <text class="principle" x="785" y="677" textLength="280" lengthAdjust="spacingAndGlyphs">LET THE OTHER PERSON DO A GREAT DEAL OF THE TALKING</text>
    <text class="principle" x="785" y="710" textLength="286" lengthAdjust="spacingAndGlyphs">LET THE OTHER PERSON FEEL THAT THE IDEA IS HIS OR HERS</text>
    <text class="principle" x="785" y="743" textLength="359" lengthAdjust="spacingAndGlyphs">TRY HONESTLY TO SEE THINGS FROM THE OTHER PERSON'S POINT OF VIEW</text>
    <text class="principle" x="785" y="776" textLength="319" lengthAdjust="spacingAndGlyphs">BE SYMPATHETIC WITH THE OTHER PERSON'S IDEAS AND DESIRES</text>
    <text class="principle" x="785" y="809" textLength="165" lengthAdjust="spacingAndGlyphs">APPEAL TO THE NOBLER MOTIVES</text>
    <text class="principle" x="785" y="843" textLength="119" lengthAdjust="spacingAndGlyphs">DRAMATIZE YOUR IDEAS</text>
    <text class="principle" x="785" y="876" textLength="137" lengthAdjust="spacingAndGlyphs">THROW DOWN A CHALLENGE</text>
  </g>

  <g class="hub hub-leader" transform="translate(100 275)">
    <circle class="hub-ring-outer" r="96"/>
    <circle class="hub-ring-mid" r="90" filter="url(#glow)"/>
    <circle class="hub-ring-band" r="82"/>
    <circle class="hub-disc" r="77"/>
    <circle class="hub-ring-inner" r="76"/>
    <text class="hub-title" font-size="38" y="-20" textLength="82" lengthAdjust="spacingAndGlyphs">BEING</text>
    <text class="hub-title" font-size="38" y="14">A</text>
    <text class="hub-title" font-size="38" y="50" textLength="102" lengthAdjust="spacingAndGlyphs">LEADER</text>
  </g>

  <g class="hub hub-fundamentals" transform="translate(672 272)">
    <circle class="hub-ring-outer" r="96"/>
    <circle class="hub-ring-mid" r="90" filter="url(#glow)"/>
    <circle class="hub-ring-band" r="82"/>
    <circle class="hub-disc" r="77"/>
    <circle class="hub-ring-inner" r="76"/>
    <text class="hub-title" font-size="20" y="-23" textLength="110" lengthAdjust="spacingAndGlyphs">FUNDAMENTAL</text>
    <text class="hub-title" font-size="20" y="-1" textLength="92" lengthAdjust="spacingAndGlyphs">TECHNIQUES</text>
    <text class="hub-title" font-size="20" y="21">IN</text>
    <text class="hub-title" font-size="20" y="43" textLength="134" lengthAdjust="spacingAndGlyphs">HANDLING PEOPLE</text>
  </g>

  <g class="hub hub-liking" transform="translate(98 660)">
    <circle class="hub-ring-outer" r="96"/>
    <circle class="hub-ring-mid" r="90" filter="url(#glow)"/>
    <circle class="hub-ring-band" r="82"/>
    <circle class="hub-disc" r="77"/>
    <circle class="hub-ring-inner" r="76"/>
    <text class="hub-title" font-size="33" y="-24" textLength="94" lengthAdjust="spacingAndGlyphs">MAKING</text>
    <text class="hub-title" font-size="33" y="10" textLength="88" lengthAdjust="spacingAndGlyphs">PEOPLE</text>
    <text class="hub-title" font-size="33" y="44" textLength="102" lengthAdjust="spacingAndGlyphs">LIKE YOU</text>
  </g>

  <g class="hub hub-persuasion" transform="translate(665 660)">
    <circle class="hub-ring-outer" r="96"/>
    <circle class="hub-ring-mid" r="90" filter="url(#glow)"/>
    <circle class="hub-ring-band" r="82"/>
    <circle class="hub-disc" r="77"/>
    <circle class="hub-ring-inner" r="76"/>
    <text class="hub-title" font-size="26" y="-36" textLength="40" lengthAdjust="spacingAndGlyphs">WIN</text>
    <text class="hub-title" font-size="26" y="-8" textLength="70" lengthAdjust="spacingAndGlyphs">PEOPLE</text>
    <text class="hub-title" font-size="26" y="20" textLength="112" lengthAdjust="spacingAndGlyphs">TO YOUR WAY</text>
    <text class="hub-title" font-size="26" y="48" textLength="116" lengthAdjust="spacingAndGlyphs">OF THINKING</text>
  </g>
</svg>
</body>
</html>
```